Driver License Monitoring Application Marketing Website

We need a new web design for our web application. The product is called "PermitSentry." We provide a driver license monitoring service to companies and local government bodies with driver fleets. Our current website is available at www.PermitSentry-demo.net.

I prefer a clean, single-page design with good SEO. Attached are some PDFs with data about the project.

Target Market(s)

Companies with driver fleets, local government.

Industry/Entity Type

Government

Coding

Coded - Design and coding required

Number of Pages Required

1 page

Colors
000000

Requirements
Must have
• Content from current www.PermitSentry-demo.net and attached PDFs.
Nice to have
• Prefer a simple Bootstrap or similar design for easy editing.
• Room for a simple video explanation of how the product works (we don't have an actual video yet)

```html
<!DOCTYPE html>
<html lang="en">
<head>
<meta charset="utf-8">
<title>PermitSentry – Florida Driver License Monitoring</title>
<link href="https://fonts.googleapis.com/css2?family=Lato:wght@300;400;700&display=swap" rel="stylesheet">
<style>
:root{
  --red:#b8232a;
  --red-bright:#e0262e;
  --black:#000;
  --ink:#222;
  --muted:#444;
  --card:#efefef;
  --footer:#2b2b2b;
  --footer-deep:#1e1e1e;
  --footer-text:#d6d6d6;
  --white:#fff;
}
*{box-sizing:border-box;margin:0;padding:0}
html,body{width:686px;height:1200px;overflow:hidden}
body{font-family:"Lato",Arial,sans-serif;color:var(--ink);background:var(--white);position:relative}
.site-header{height:68px;border-top:3px solid var(--red);border-bottom:3px solid var(--black);display:flex;align-items:center;padding:0 50px;justify-content:space-between}
.brand{font-size:17px;font-weight:700;letter-spacing:.3px;color:var(--black)}
.main-nav{display:flex;gap:12px;font-size:8px;font-weight:700;align-items:center}
.main-nav a{color:var(--ink);text-decoration:none}
.main-nav a.is-active{color:var(--red)}
.search-icon{margin-left:16px}
.hero{position:relative;height:322px;background:linear-gradient(100deg,#cfd8df 0%,#e9eef2 40%,#8e9299 60%,#5e6167 100%)}
.hero-photo{position:absolute;inset:0}
.hero-card{position:absolute;left:50px;top:21px;width:306px}
.hero-title{background:var(--red);height:128px;display:flex;align-items:center}
.state-shape{width:112px;height:100%;display:block}
.hero-title h1{font-weight:400;font-size:27px;line-height:29px;color:var(--white)}
.hero-body{background:var(--black);height:62px;padding:11px 14px;font-size:9px;line-height:11.5px;color:var(--white)}
.hero-body em{font-style:normal;color:var(--red-bright)}
.hero-btn{position:absolute;right:8px;bottom:-11px;width:103px;height:34px;background:var(--red);color:var(--white);text-align:center;padding-top:5px}
.hero-btn strong{display:block;font-size:10px}
.hero-btn span{display:block;font-size:7px;font-weight:700;margin-top:3px}
.question-band{height:66px;background:var(--black);color:var(--white);display:flex;align-items:center;justify-content:center;font-size:16.5px;font-weight:700}
.question-band em{font-style:normal;color:var(--red-bright)}
.intro{display:flex;padding:40px 50px 0;height:242px}
.video{width:260px;height:173px;background:linear-gradient(180deg,#b9c3cc 0%,#dfe2e3 40%,#c9b43a 60%,#6e6e68 85%);position:relative}
.video-bar{position:absolute;left:0;right:0;bottom:0;height:13px;background:#111;display:flex;align-items:center;padding:0 8px;gap:8px;color:#bbb;font-size:5px}
.video-play{position:absolute;left:118px;top:70px}
.intro-text{margin-left:25px;padding-top:22px}
.intro-text h2{font-size:16.5px;font-weight:400;color:var(--red)}
.intro-text h3{font-size:10px;font-weight:700;color:var(--muted);margin:8px 0 15px}
.intro-text p{font-size:8px;line-height:10.8px;color:var(--muted);width:270px}
.read-more{display:inline-flex;margin-top:18px;height:15px;font-size:7px;font-weight:700;color:var(--white)}
.read-more i{width:15px;background:#222;display:flex;align-items:center;justify-content:center;font-style:normal}
.read-more span{background:var(--red);padding:0 8px;display:flex;align-items:center}
.cards{display:flex;gap:5px;padding:0 50px;height:116px}
.card{flex:1;background:var(--card);border-bottom:2px solid #999;text-align:center}
.card-photo{height:58px}
.card h4{font-size:13px;font-weight:400;color:var(--red);margin-top:12px}
.card p{font-size:10.5px;font-weight:300;color:var(--ink);margin-top:3px}
.cta{margin:16px 50px 0;height:48px;background:var(--red);border-bottom:3px solid #2b2b2b;color:var(--white);display:flex;align-items:center;justify-content:center;gap:10px;font-size:19px;font-weight:700}
.alerts{text-align:center;padding-top:24px}
.alerts h2{font-size:16.5px;font-weight:300;color:var(--red);margin-bottom:14px}
.tag-row{display:flex;justify-content:center;gap:5px;margin-bottom:3px}
.tag{border:1px solid #ccc;font-size:11px;height:17px;line-height:15px;padding:0 4px;color:var(--ink)}
.site-footer{position:absolute;left:0;top:1078px;width:686px;height:122px;background:var(--footer);color:var(--footer-text)}
.footer-rule{position:absolute;left:50px;right:61px;top:0;height:2px;background:var(--red)}
.footer-brand{position:absolute;left:52px;top:15px;font-size:15px;font-weight:700;color:var(--white)}
.footer-contact{position:absolute;left:52px;top:38px;font-size:7.5px;line-height:9.6px}
.footer-col{position:absolute;top:23px;font-size:7.5px;line-height:12px}
.footer-col h5{font-size:7.5px;font-weight:700;color:var(--white);margin-bottom:4px}
.footer-col .is-active{color:var(--red-bright)}
.footer-mark{position:absolute;left:494px;top:16px;width:130px;height:78px}
.footer-mark-shape{position:absolute;left:0;top:0;width:80px;height:78px;background:linear-gradient(135deg,#b8232a,#7e1a1e);border-radius:4px}
.footer-mark p{position:absolute;left:13px;top:14px;font-size:13px;font-weight:300;line-height:15.5px;color:var(--white)}
.footer-bottom{position:absolute;left:0;bottom:0;width:100%;height:18px;background:var(--footer-deep);display:flex;align-items:center;justify-content:space-between;padding:0 50px;font-size:7px;color:#777}
</style>
</head>
<body>
<header class="site-header">
  <div class="brand">PermitSentry</div>
  <nav class="main-nav">
    <a class="is-active" href="#">HOME</a>
    <a href="#">LICENSE MONITORING</a>
    <a href="#">ABOUT US</a>
    <a href="#">CONTACT</a>
    <a href="#">CLIENT LOGIN</a>
    <svg class="search-icon" width="9" height="9" viewBox="0 0 10 10"><circle cx="4" cy="4" r="3" fill="none" stroke="#333" stroke-width="1.3"/><line x1="6.3" y1="6.3" x2="9" y2="9" stroke="#333" stroke-width="1.3"/></svg>
  </nav>
</header>

<section class="hero">
  <div class="hero-photo" role="img" aria-label="Smiling truck driver in a grey cap and uniform seated at the wheel of a white van"></div>
  <div class="hero-card">
    <div class="hero-title">
      <div class="state-shape" role="img" aria-label="Outline map of the state of Florida"></div>
      <h1>Florida<br>driver license<br>monitoring</h1>
    </div>
    <div class="hero-body">
      Monitor your fleet <em>electronically</em>. Get alerts by <em>email</em> and <em>online</em>.<br>
      Never let another unlicensed or<br>unauthorized driver behind the wheel
    </div>
    <a class="hero-btn"><strong>MORE INFO &nbsp;›</strong><span>TRACK YOUR FLEET</span></a>
  </div>
</section>

<div class="question-band"><p>How many of your drivers currently have a <em>suspended</em> license?</p></div>

<section class="intro">
  <div class="video" role="img" aria-label="Video placeholder showing a yellow semi truck with a tanker trailer">
    <svg class="video-play" width="24" height="28" viewBox="0 0 24 28"><polygon points="0,0 24,14 0,28" fill="#c8252c"/></svg>
    <div class="video-bar"><span>▶</span><span>0:05 / 2:24</span></div>
  </div>
  <div class="intro-text">
    <h2>License Monitoring</h2>
    <h3>Monitor your drivers electronically, twenty-four hours a day.</h3>
    <p>How many of your drivers currently have a suspended license? The answer may surprise you. Driving with a suspended license is the most commonly committed offense in America. In 2011, over 1.8 million licenses got suspended in Florida. With just over 15 million drivers, that's 12% of all licensed Florida drivers.</p>
    <a class="read-more"><i>›</i><span>READ MORE</span></a>
  </div>
</section>

<section class="cards">
  <article class="card"><div class="card-photo" role="img" aria-label="Driver in a red shirt at a truck steering wheel" style="background:linear-gradient(135deg,#5e8a4a,#b33a35 60%,#333)"></div><h4>What We Do</h4><p>License Monitoring</p></article>
  <article class="card"><div class="card-photo" role="img" aria-label="Blue commercial truck with a white trailer" style="background:linear-gradient(135deg,#cfd6de,#3e5a8c 60%,#28324a)"></div><h4>Commercial</h4><p>Private Sector</p></article>
  <article class="card"><div class="card-photo" role="img" aria-label="Red and white state flag" style="background:linear-gradient(135deg,#c8262c,#f3eeee 50%,#c8262c)"></div><h4>Government</h4><p>Public Sector</p></article>
  <article class="card"><div class="card-photo" role="img" aria-label="Driver holding a road map giving a thumbs up" style="background:linear-gradient(135deg,#9db3c8,#c4a37f 55%,#4a4a4a)"></div><h4>About Us</h4><p>Florida Law Authorities</p></article>
</section>

<div class="cta">CONTACT US FOR A PRODUCT DEMONSTRATION <svg width="10" height="14" viewBox="0 0 10 14"><polyline points="2,2 8,7 2,12" fill="none" stroke="#fff" stroke-width="2.2"/></svg></div>

<section class="alerts">
  <h2>Get Instant Alert for</h2>
  <div class="tag-row"><span class="tag">Suspensions for Child Support</span><span class="tag">Suspensions for Unpaid Fines</span><span class="tag">Suspensions for Court Obligations</span></div>
  <div class="tag-row"><span class="tag">Revocations for Accidents</span><span class="tag">Revocations for Convictions</span></div>
  <div class="tag-row"><span class="tag">Commercial Vehicle Desqualifications</span><span class="tag">Medical Certificate Expirations</span></div>
  <div class="tag-row"><span class="tag">License Expirations</span><span class="tag">License Cancellations</span></div>
  <div class="tag-row"><span class="tag">All Other License Sanctions</span></div>
</section>

<footer class="site-footer">
  <div class="footer-rule"></div>
  <div class="footer-brand">PermitSentry</div>
  <address class="footer-contact" style="font-style:normal">
    PermitSentry, Inc.<br>1450 Harbor Point Ave., Ste 210<br>Coral Bay, FL 33099<br>T 1.555.010.2040<br>F 1.555.010.2041<br>contact@permitsentry-demo.net
  </address>
  <div class="footer-col" style="left:277px">
    <h5>NAVIGATIONS</h5>
    <div class="is-active">Home</div><div>License Monitoring</div><div>About Us</div><div>Contact</div><div>Client Login</div>
  </div>
  <div class="footer-col" style="left:379px">
    <h5>OUR SERVICES FOR</h5>
    <div>Commmecial</div><div>Government</div>
  </div>
  <div class="footer-mark">
    <div class="footer-mark-shape" role="img" aria-label="Red map of the state of Florida"></div>
    <p>FLORIDA<br>DRIVER LICENSE<br>MONITORING</p>
  </div>
  <div class="footer-bottom"><span>Copyright © 2015 PermitSentry-demo.net</span><span>Privacy Policy</span></div>
</footer>
</body>
</html>
```